Lumeno-Interior design firm
Hello all,
I will announce the winner in the next few hours...
I appreciate your AMAZING ideas and all the many revisions that each of you submited, they helped us to understand your creative proposals and at the end to select a winner.
THANK YOU!
Lumeno Design
Draft #317 and #318
We are looking at some winning designs already and we will send our efforts towards those. i appreciate your entry very much.
Thanks!
Draft #312
The font on the subject LUMENO Interior design firm needs to be changed. I dont like it. I like the font used on the HOME, PORTFOLIO, etc...main subjects if that helps!
Everything else looks amazing!
hi all,
I had an unexpected business to attend today and I was not able to complete the feedback to all of you. We decided to extend the time to provide the missing feedback...I will provide to all, just give me some time.
I have decided to extend the contest. This was a last minute descision.
I appreciate your entry but is not what I am looking for. I don't want to waste your time as well as I prefer to concentrate on the designs/designers that have invested some time with me already.
Thank you and I appreciate your understanding!
Thanks brightquill! I really appreciate your understanding!
Draft #273
Can you justified all the texts used on each page? That will be great for final review.
Drafts #270 and #272
the text needs to be justified and that will make it!
Draft #269
HOME
There is a small misspell at the bottom left...it reads Lemeno instead of Lumeno.
Ater that revision you are set!
@PH, Thanks for your comments...
Dear Brightquill,
I like your entry but i am sorry to say that there is nothing original about it. I feel respect for everyones work and even when I am not an expert I feel you are copying other entries. I can not give you credit for someone else's ideas and I would appreciate if you come up with the same concept but with something that is your very own creation.
With all my respect...
Draft #251
Looks good just to revise the "yellow" cubes to be softer...and also please use my pictures for each page so I can compare with everyone else.
Thank you so much!
Draft #250
I would prefer to container the ABOUT US description on within the limits of the cubes so if necessary lets remove the "yellow" cubes so we can move up the wording and fit it within...
Use the service wording as reference...it is contained and it does not go below the "cubes"
Draft #249
lets list the services on a horizontal way inside the "cubes" Makes sense? linear way showing the services and the main wording as is.
Draft #248
can we made the windows with tabs LIVING, DINING, BEDROOM ACCENTS and KIDS to be one of the "cubes" from your design?
maybe using the bottom five...?
then when you click on I would like to see a complete picture...hopefully you come up with an idea but if not we can look at it together after revision...
Thanks
Draft #247
My only change is the "yellow" buttons to be more with softer colors...soft grey/white...or any suggestions within my request.
Draft #234
Wording needs to be consistent...I prefer white please revise.
Draft #227
Revisions:
I dont like the phone image under phone, please remove
Please do not underline the website
I prefer just letter on the front:
P: for phone
W: for website
etc...
In your case I would prefer not to use my picture...lets just remove it and after all this it should be done!
Looking good!
Draft #223
I need you to add the wording that I sent for services as well...it is important!
Thanks! Everything else looks perfect!
Hello@PH
I`m just waiting for your Feedback on
#221(Home page), #222(Portfolio Page), #223(Services Page),#224(About Us Page), & #225(Contact Page)
Zora
FOR EVERYONE:
PLEASE submit your complete designs, I wont be extending the project and with the time left I wont be able to give feedback and revisions to detail to everyone.
I really appreciate your hard work on attention to my project.
You ALL are very talented!
Good luck!
Draft #208 you can move forward with the inner pages.
Draft #207
I need the text to be justified please. You can complete your design with all he pages, I like the layout as is.
Look forward to final entries.

```html
<!DOCTYPE html>
<html lang="en">
<head>
<meta charset="utf-8">
<title>Lumeno – Services</title>
<link rel="stylesheet" href="https://fonts.googleapis.com/css2?family=Arimo:wght@400;700&display=swap">
<style>
  :root {
    --page: #ffffff;
    --page-tint: #f7f4ef;
    --ink: #1f1b18;
    --ink-soft: #4a4440;
    --ink-muted: #8a837c;
    --veil: rgba(255, 255, 255, 0.55);
    --veil-strong: rgba(255, 255, 255, 0.62);
    --divider: rgba(255, 255, 255, 0.85);
    --frame: #c9c5c0;
    --photo-light: #ece5dc;
    --photo-mid: #d3c3ae;
    --photo-dark: #5e4a3d;
    --photo-deep: #3f3129;
    --chip: #9d9890;
  }
  * { box-sizing: border-box; margin: 0; padding: 0; }
  html, body { width: 1200px; height: 886px; overflow: hidden; }
  body {
    position: relative;
    background: radial-gradient(ellipse at 50% 40%, var(--page) 55%, var(--page-tint) 100%);
    font-family: "Arimo", Arial, sans-serif;
    color: var(--ink);
  }

  /* Header */
  .brand {
    position: absolute; left: 176px; top: 34px;
  }
  .brand-name {
    font-size: 44px; font-weight: 700; line-height: 1;
    color: var(--ink);
  }
  .brand-tagline {
    font-size: 15px; color: var(--ink-soft); margin-top: 8px;
  }

  /* Main stage */
  .stage {
    position: absolute; left: 144px; top: 120px; width: 912px; height: 648px;
    border: 3px solid var(--frame);
    box-shadow: 0 2px 8px rgba(0,0,0,0.18);
    overflow: hidden;
  }
  .stage-photo {
    position: absolute; inset: 0;
    background: linear-gradient(90deg, var(--photo-light) 0%, var(--photo-mid) 38%, var(--photo-dark) 62%, var(--photo-deep) 100%);
  }
  .stage-columns { position: absolute; inset: 0; }
  .column-line {
    position: absolute; top: 0; bottom: 0; width: 4px; background: var(--divider);
  }

  .services-panel {
    position: absolute; left: 182px; top: 192px; width: 545px; height: 306px;
    background: var(--veil);
    padding: 18px 24px 0 26px;
  }
  .services-title { font-size: 21px; font-weight: 400; letter-spacing: 0.5px; color: var(--ink); }
  .services-lists { display: flex; margin-top: 10px; }
  .service-list { list-style: none; font-size: 16px; line-height: 24px; color: var(--ink-soft); }
  .service-list:first-child { width: 269px; margin-top: 4px; }
  .service-list li { display: flex; align-items: center; gap: 9px; }
  .service-list li::before {
    content: ""; width: 10px; height: 10px; border-radius: 50%;
    border: 1.5px solid var(--ink-muted); background: rgba(255,255,255,0.6);
  }
  .services-copy {
    margin-top: 12px; font-size: 14px; line-height: 23px; text-align: justify;
    color: var(--ink-soft);
  }

  .main-nav {
    position: absolute; left: 0; right: 0; top: 498px; height: 144px;
    background: var(--veil-strong);
    display: flex;
  }
  .nav-item {
    flex: 1; display: flex; align-items: center; justify-content: center;
    font-size: 29px; letter-spacing: -0.8px; color: var(--ink); text-decoration: none;
    padding-bottom: 14px; white-space: nowrap;
  }
  .nav-item.is-current { color: var(--ink-muted); }

  /* Footer */
  .legal {
    position: absolute; left: 161px; top: 796px;
    font-size: 12px; line-height: 22px; color: var(--ink-soft);
  }
  .social {
    position: absolute; left: 886px; top: 790px;
    display: flex; align-items: center; gap: 12px; font-size: 13px; color: var(--ink-soft);
  }
  .social-link { display: flex; align-items: center; gap: 5px; color: var(--ink-soft); text-decoration: none; }
  .social-chip { width: 22px; height: 22px; border-radius: 4px; background: var(--chip); }
</style>
</head>
<body>

<header class="brand">
  <div class="brand-name">Lumeno</div>
  <div class="brand-tagline">Interiors, architecture and art</div>
</header>

<main class="stage">
  <div class="stage-photo" role="img" aria-label="Interior photograph: a tufted leather armchair with a sequined cushion beside a wooden side table"></div>
  <div class="stage-columns" aria-hidden="true">
    <span class="column-line" style="left:180px"></span>
    <span class="column-line" style="left:362px"></span>
    <span class="column-line" style="left:544px"></span>
    <span class="column-line" style="left:726px"></span>
  </div>

  <section class="services-panel">
    <h1 class="services-title">SERVICES</h1>
    <div class="services-lists">
      <ul class="service-list">
        <li>Interior Design</li>
        <li>Architectural Consulting</li>
        <li>Art Selection</li>
      </ul>
      <ul class="service-list">
        <li>Textiles</li>
        <li>Furniture Import and Export</li>
        <li>Staging</li>
        <li>Accessories</li>
      </ul>
    </div>
    <p class="services-copy">As an additional service, we offer a turn-key design service that integrates all elements of interior and exterior design including space planning, furnishing, lighting and decor. We will take care of purchasing everything from the linens to the flowers, hang your art pieces, and purchase your chise so when you get to your new home, the beds are made, the candles are lit and everything is in place to live and enjoy!</p>
  </section>

  <nav class="main-nav">
    <a class="nav-item" href="#">HOME</a>
    <a class="nav-item" href="#">PORTFOLIO</a>
    <a class="nav-item is-current" href="#">SERVICES</a>
    <a class="nav-item" href="#">ABOUT US</a>
    <a class="nav-item" href="#">CONTACT</a>
  </nav>
</main>

<footer>
  <div class="legal">
    <p>Copyright © 2011 LUMENO - Interior Design Firm &nbsp;|&nbsp; All Rights Reserved</p>
    <p>Site by : Brightpixel.net</p>
  </div>
  <div class="social">
    <span>Follow Us:</span>
    <a class="social-link" href="#"><span class="social-chip"></span>Friendly</a>
    <a class="social-link" href="#"><span class="social-chip"></span>Chirper</a>
  </div>
</footer>

</body>
</html>
```